Presentation Folder, for Cancer Awareness, VERY COLORFULL AND MODERN

This will be a standard size folder that will hold standard 8 1/2 x 11 papers with a business card slot on the flap, this is a very easy project with very little text and the design for the back page is already done so all you really have to do is make a very nice colorful front cover, you will see my attachments are labeled and I gave you alot of instructions, this should be a very fast easy project
Updates

Reason: there has not been enough quality designs, sorry

Target Market(s)

Our Target Market is Dr's that Deal with Cancer patients

Industry/Entity Type

Healthcare

Font styles to use
Serif

Colors

Designer to choose colors to be used in the design.

Requirements
Must have
• Project must be tasteful and look professional with the ribbons as the main focal point in the center of folder the folder should be a nice gray color to accent the color of the ribbons , the back page needs no design it is the" Velmora Test" in the attachments I sent
Nice to have
• I would like the ribbons displayed in a row, I included a logo sample layout
• a picture on the front of the folder under the words Hereditary Cancer Screening - Then under that put the words - The Power of Knowledge - then add the picture I labeled Great Picture in the attachments

```html
<!DOCTYPE html>
<html lang="en">
<head>
<meta charset="utf-8">
<title>Hereditary Cancer Screening – Presentation Folder</title>
<link rel="stylesheet" href="https://fonts.googleapis.com/css2?family=Arimo:ital,wght@0,400;0,700;1,700&family=Crimson+Text:wght@400;600;700&family=Merriweather:wght@700&display=swap">
<style>
  :root{
    --paper:#ffffff;
    --dieline:#9a9a9a;
    --ink:#2b2b2b;
    --ink-soft:#6a6a6a;
    --brand-red:#e63a2e;
    --title-blue:#5aafe0;
    --frame-blue:#4fa8dd;
    --row-band:#ececec;
    --lynch:#f6bd3c;
    --peutz:#a9c94a;
    --lifraumeni:#3aa756;
    --cowden:#1b9ad6;
    --hdgc:#6b6b6b;
  }
  *{margin:0;padding:0;box-sizing:border-box}
  html,body{width:1200px;height:976px;overflow:hidden;background:var(--paper)}
  .folder{position:relative;width:1200px;height:976px;font-family:"Arimo",Arial,sans-serif;color:var(--ink)}
  .dieline{position:absolute;left:0;top:0}

  /* back panel header */
  .brand-block{position:absolute;left:130px;top:88px}
  .brand-name{font-family:"Arimo",Arial,sans-serif;font-size:15px;letter-spacing:4px;color:var(--ink-soft);font-weight:400;white-space:nowrap}
  .brand-contact{font-size:5px;line-height:6.5px;color:var(--ink);margin-top:3px;font-weight:700;white-space:nowrap}
  .menu-title{position:absolute;left:310px;top:87px;width:220px;text-align:right;white-space:nowrap;font-style:italic;font-weight:700;font-size:14.5px;line-height:17px;color:var(--brand-red)}
  .menu-title sup{font-size:7px;line-height:0}
  .menu-ref{position:absolute;left:330px;top:115px;width:198px;text-align:right;white-space:nowrap;font-size:5px;font-weight:700;color:var(--ink)}

  /* gene table */
  .gene-table{position:absolute;left:203px;top:143px;width:249px}
  .row{display:flex;height:12.25px;line-height:12.25px;font-size:6.2px;font-weight:700;white-space:nowrap}
  .row.alt{background:var(--row-band)}
  .gene{width:78px;padding-left:5px;color:var(--brand-red)}
  .gene.indent{padding-left:12px}
  .organ{flex:1;color:var(--ink)}
  .row.head{color:#fff;font-weight:700;text-transform:uppercase}
  .row.head .gene,.row.head .organ{color:#fff}
  .row.head.main{background:var(--brand-red)}
  .row.section{padding-left:12px;color:#fff;text-transform:uppercase}
  .section.lynch{background:var(--lynch)}
  .section.peutz{background:var(--peutz)}
  .section.lifraumeni{background:var(--lifraumeni)}
  .section.cowden{background:var(--cowden)}
  .section.hdgc{background:var(--hdgc)}

  /* front cover */
  .cover-logo{position:absolute;left:770px;top:86px;width:200px;text-align:center}
  .cover-logo .dot{display:block;width:17px;height:17px;border-radius:50%;background:var(--brand-red);margin:0 auto 4px}
  .cover-logo .name{font-family:"Arimo",Arial,sans-serif;font-size:8px;letter-spacing:2px;color:var(--ink-soft);text-transform:uppercase}
  .cover-title{position:absolute;left:600px;top:142px;width:540px;text-align:center;white-space:nowrap;font-family:"Merriweather",Georgia,serif;font-weight:700;font-size:28px;color:var(--title-blue)}
  .cover-subtitle{position:absolute;left:600px;top:179px;width:540px;text-align:center;white-space:nowrap;font-family:"Crimson Text",Georgia,serif;font-size:22px;color:var(--ink)}
  .photo-frame{position:absolute;left:769px;top:280px;width:205px;height:135px;border:2px solid var(--frame-blue);background:#fff;padding:5px}
  .photo-frame .photo{width:100%;height:100%;border:1px solid var(--frame-blue);background:linear-gradient(135deg,#f4f4f4 0%,#d9c3ae 45%,#b7b9bd 100%)}
  .ribbon-row{position:absolute;left:660px;top:432px;width:418px;height:68px;border-radius:6px;
    background:linear-gradient(90deg,#f2c14e 0%,#9a9a9a 8%,#e36fb4 15%,#2a8fa6 22%,#93c6e8 29%,#7a3fa0 36%,#2a3f9a 43%,#6b3c1e 50%,#f08f7a 57%,#34a853 64%,#2a3f9a 71%,#e6e6e6 78%,#2a2a2a 85%,#1a8f9a 90%,#5ab0e0 95%,#8d93e0 100%)}
  .cancer-list{position:absolute;left:600px;top:517px;width:550px;text-align:center;font-family:"Crimson Text",Georgia,serif;font-size:13px;line-height:14px;color:var(--ink)}

  /* flaps */
  .flap-statement{position:absolute;left:727px;top:795px;width:400px;text-align:center;transform:rotate(180deg);font-family:"Crimson Text",Georgia,serif;font-size:12px;line-height:13.5px;color:var(--brand-red)}
  .flap-statement span{display:block;white-space:nowrap}
  .card-partner{position:absolute;left:222px;top:808px;width:200px;text-align:center;transform:rotate(180deg);font-family:"Crimson Text",Georgia,serif;color:var(--ink-soft)}
  .card-partner .partner{display:block;font-size:13px;font-weight:700;letter-spacing:.5px;white-space:nowrap}
  .card-partner .note{display:block;font-size:9px;white-space:nowrap}
</style>
</head>
<body>
<div class="folder">
  <svg class="dieline" width="1200" height="976" viewBox="0 0 1200 976" aria-hidden="true">
    <defs>
      <linearGradient id="cover-shade" x1="0" y1="0" x2="0" y2="1">
        <stop offset="0" stop-color="#fbfbfb"/>
        <stop offset="0.45" stop-color="#e8e9eb"/>
        <stop offset="0.72" stop-color="#eef0f1"/>
        <stop offset="1" stop-color="#ffffff"/>
      </linearGradient>
      <clipPath id="folder-shape">
        <path d="M30,12 L1176,12 Q1188,12 1188,24 L1188,432 A14 14 0 0 0 1188,460 L1188,690 L1184,720 L1184,936 Q1184,952 1168,952 L640,952 Q620,952 618,940 L602,702 Q600,694 598,702 L582,940 Q580,952 562,952 L80,952 Q64,952 64,936 L64,720 L18,690 L18,472 A14 14 0 0 0 18,444 L18,24 Q18,12 30,12 Z"/>
      </clipPath>
    </defs>
    <path d="M30,12 L1176,12 Q1188,12 1188,24 L1188,432 A14 14 0 0 0 1188,460 L1188,690 L1184,720 L1184,936 Q1184,952 1168,952 L640,952 Q620,952 618,940 L602,702 Q600,694 598,702 L582,940 Q580,952 562,952 L80,952 Q64,952 64,936 L64,720 L18,690 L18,472 A14 14 0 0 0 18,444 L18,24 Q18,12 30,12 Z" fill="#ffffff"/>
    <rect x="600" y="0" width="600" height="976" fill="url(#cover-shade)" clip-path="url(#folder-shape)"/>
    <path d="M30,12 L1176,12 Q1188,12 1188,24 L1188,432 A14 14 0 0 0 1188,460 L1188,690 L1184,720 L1184,936 Q1184,952 1168,952 L640,952 Q620,952 618,940 L602,702 Q600,694 598,702 L582,940 Q580,952 562,952 L80,952 Q64,952 64,936 L64,720 L18,690 L18,472 A14 14 0 0 0 18,444 L18,24 Q18,12 30,12 Z" fill="none" stroke="var(--dieline)" stroke-width="1"/>
    <g class="card-slot" stroke="#333" stroke-width="1">
      <line x1="228" y1="800" x2="258" y2="770"/>
      <line x1="396" y1="768" x2="428" y2="800"/>
      <line x1="228" y1="853" x2="258" y2="885"/>
      <line x1="396" y1="885" x2="428" y2="853"/>
    </g>
  </svg>

  <!-- back panel -->
  <div class="brand-block">
    <div class="brand-name">GENEVIALABS</div>
    <div class="brand-contact">820 HARROW LANE | SUITE B | MARLOWE, GA 30400<br>(tel) 555.014.2290 | (fax) 555.014.2291 | care@genevialabs.net</div>
  </div>
  <div class="menu-title">VELMORA<sup>™</sup> Test Menu</div>
  <div class="menu-ref">CLIA# 00D0000000 | GENEVIALABS.NET</div>

  <div class="gene-table">
    <div class="row head main"><span class="gene">Gene</span><span class="organ">Cancer-Associated Organ/Systems</span></div>
    <div class="row"><span class="gene">APC</span><span class="organ">Colon</span></div>
    <div class="row alt"><span class="gene">ATM</span><span class="organ">Breast/Pancreatic/Brain</span></div>
    <div class="row"><span class="gene">BARD1</span><span class="organ">Breast/Ovarian</span></div>
    <div class="row alt"><span class="gene">BMPR1A</span><span class="organ">Colon</span></div>
    <div class="row"><span class="gene">BRCA1</span><span class="organ">Breast/Ovarian/Prostate</span></div>
    <div class="row alt"><span class="gene">BRCA2</span><span class="organ">Breast/Ovarian/Prostate</span></div>
    <div class="row"><span class="gene">BRIP1</span><span class="organ">Breast/Ovarian</span></div>
    <div class="row alt"><span class="gene">CDK4</span><span class="organ">Melanoma</span></div>
    <div class="row"><span class="gene">P16 (CDKN2A)</span><span class="organ">Melanoma/Breast/Pancreatic/Squamous</span></div>
    <div class="row alt"><span class="gene">FANCC</span><span class="organ">Blood</span></div>
    <div class="row"><span class="gene">MEN1</span><span class="organ">Thyroid/Parathyroid</span></div>
    <div class="row alt"><span class="gene">MET</span><span class="organ">Renal/Hepatic</span></div>
    <div class="row"><span class="gene">MRE11A</span><span class="organ">Ovarian/Breast</span></div>
    <div class="row alt"><span class="gene">NBN</span><span class="organ">Breast/Ovarian/Prostate/Melanoma</span></div>
    <div class="row"><span class="gene">NF1</span><span class="organ">Blood</span></div>
    <div class="row alt"><span class="gene">NTRK1</span><span class="organ">Thyroid/Parathyroid</span></div>
    <div class="row"><span class="gene">PALB2</span><span class="organ">Breast/Ovarian/Pancreatic</span></div>
    <div class="row alt"><span class="gene">PTCH1</span><span class="organ">Melanoma/Brain/Breast/Colon</span></div>
    <div class="row"><span class="gene">RAD50</span><span class="organ">Breast/Ovarian</span></div>
    <div class="row alt"><span class="gene">RAD51C</span><span class="organ">Ovarian/Breast</span></div>
    <div class="row"><span class="gene">RAD51D</span><span class="organ">Ovarian/Breast</span></div>
    <div class="row alt"><span class="gene">RET</span><span class="organ">Lung/Thyroid/Parathyroid</span></div>
    <div class="row"><span class="gene">SMAD4</span><span class="organ">Colon/Pancreas</span></div>
    <div class="row section lynch">Lynch Syndrome Genes</div>
    <div class="row"><span class="gene indent">MLH1</span><span class="organ">Colorectal/Ovarian</span></div>
    <div class="row alt"><span class="gene indent">MSH2</span><span class="organ">Colorectal/Ovarian</span></div>
    <div class="row"><span class="gene indent">MSH6</span><span class="organ">Colorectal/Ovarian</span></div>
    <div class="row alt"><span class="gene indent">PMS2</span><span class="organ">Colorectal/Ovarian</span></div>
    <div class="row"><span class="gene indent">EPCAM</span><span class="organ">Colorectal</span></div>
    <div class="row section peutz">Peutz-Jeghers Syndrome Gene</div>
    <div class="row"><span class="gene indent">STK11</span><span class="organ">Breast/Ovarian/Melanoma/Colorectal/Lung</span></div>
    <div class="row section lifraumeni">Li-Fraumeni Syndrome Gene</div>
    <div class="row"><span class="gene indent">CHEK2</span><span class="organ">Breast/Ovarian/Prostate</span></div>
    <div class="row alt"><span class="gene indent">PT53</span><span class="organ">Breast/Bladder/Ovarian/Squamous</span></div>
    <div class="row section cowden">Cowden Syndrome Gene</div>
    <div class="row"><span class="gene indent">PTEN</span><span class="organ">Endometrium/Breast/Prostate/Lung</span></div>
    <div class="row section hdgc">Hereditary Diffuse Gastric Cancer Syndrome Gene</div>
    <div class="row"><span class="gene indent">CDH1</span><span class="organ">Breast/Gastric/Ovarian/Prostate</span></div>
    <div class="row alt"><span class="gene indent">VHL</span><span class="organ">Renal</span></div>
  </div>

  <!-- front cover -->
  <div class="cover-logo"><span class="dot"></span><span class="name">Genevia Labs</span></div>
  <h1 class="cover-title">Hereditary Cancer Screening</h1>
  <p class="cover-subtitle">The Power of Knowledge</p>
  <div class="photo-frame"><div class="photo" role="img" aria-label="Photograph of a smiling older couple embracing"></div></div>
  <div class="ribbon-row" role="img" aria-label="Row of cancer awareness ribbons in many colours"></div>
  <p class="cancer-list">Breast | Ovarian | Endometrial | Gastric | Colorectal | Pancreatic<br>Melanoma | Prostate | Lung | Colon</p>

  <!-- flaps -->
  <p class="flap-statement">
    <span>At our state of the art, CLIA certified and COLA accredited facility we perfor</span>
    <span>Next Generation Sequencing (NGS) based screening for mutations known to</span>
    <span>affect an individual's Risk of developing Hereditary Cancer. Results from the</span>
    <span>test enable the Physician to make Better informed treatment decisions.</span>
  </p>
  <p class="card-partner">
    <span class="partner">Halvern Wealth Partners</span>
    <span class="note">an independent arm of Genevia Labs LLC</span>
  </p>
</div>
</body>
</html>
```